MORVELLI TILE. CRAFTED FOR EVERY FLOOR

We need a web design for a tile company, we specialize in mostly commercial and residential projects.
With a striking and 3D look design, and stunning images of tile work.
With a touch of a silver look as my business card (last picture uploaded)
And easy to maneuver the website… (it can be Wordpress, CSS, HTML… just easy to work with)

Target Market(s)

Construction, innovating exclusive designs

Industry/Entity Type

Tile, flooring

Number of Pages Required

4 page

Font styles to use
Sans Serif

Requirements
Must have
• Elegant, Modern, professional Interior Design Web
Nice to have
• Commercial and residential stunning images as examples work

```html
<!DOCTYPE html>
<html lang="en">
<head>
<meta charset="utf-8">
<title>Morvelli Tile – Homepage Concepts</title>
<link href="https://fonts.googleapis.com/css2?family=Oranienbaum&family=Poppins:wght@400;500;600&display=swap" rel="stylesheet">
<style>
:root{
  --board:#c9c8c9;
  --brown:#5f3a3f;
  --brown-soft:#6f474b;
  --terracotta:#c96c58;
  --gray:#e7e5e5;
  --ink:#2b2324;
  --muted:#6a6264;
  --dark:#2e2d2e;
  --black:#161414;
  --white:#ffffff;
}
*{margin:0;padding:0;box-sizing:border-box}
html,body{width:677px;height:1200px;overflow:hidden;background:var(--board)}
body{font-family:"Poppins",sans-serif;color:var(--ink)}
.board{position:absolute;left:0;top:0;width:1453px;height:2576px;transform:scale(.46593);transform-origin:0 0;background:var(--board)}
.page{position:absolute;top:30px;width:688px;background:var(--white);overflow:hidden}
.page--a{left:27px;height:2445px}
.page--b{left:738px;height:2515px}
.abs{position:absolute}

/* header */
.site-header{left:0;top:0;width:688px;height:60px;background:linear-gradient(90deg,#5a373c,#6c4448 50%,#5a373c)}
.nav{top:14px;height:30px;border-top:1px solid #d9c7c8;border-bottom:1px solid #d9c7c8;display:flex;justify-content:space-between;align-items:center;padding:0 8px;font-size:8.5px;font-weight:500;color:var(--white);letter-spacing:.3px}
.nav--left{left:56px;width:210px}
.nav--right{left:421px;width:210px}
.brand{left:264px;top:18px;width:160px;text-align:center;color:var(--white);font-size:12px;letter-spacing:2.5px;font-weight:500}
.brand-mark{display:block;width:9px;height:9px;background:var(--white);margin:0 auto 5px}

/* hero */
.hero{left:0;top:60px;width:688px;height:340px;background:linear-gradient(100deg,#5d564f 0%,#3b3532 30%,#2d2a27 50%,#304542 70%,#4a3a2e 100%)}
.hero-frame{left:6px;top:4px;width:676px;height:332px;border:2px solid var(--white)}
.hero-box{left:155px;top:80px;width:380px;height:165px;background:rgba(34,26,26,.55)}
.hero-copy{left:0;top:184px;width:688px;text-align:center;color:var(--white)}
.hero-copy .kicker{font-size:11px;letter-spacing:.5px}
.hero-copy h1{font-family:"Oranienbaum",serif;font-weight:400;font-size:34px;line-height:1.15;margin:6px 0 4px}
.hero-copy p{font-size:11px;letter-spacing:.3px}
.hero-dots{left:25px;top:146px;width:6px}
.hero-dots i{display:block;width:5px;height:5px;border-radius:50%;background:var(--white);margin-bottom:6px}
.hero-dots i.on{background:var(--terracotta)}

/* section titles */
.section-title{left:0;width:688px;height:44px;text-align:center}
.section-title .ghost{position:absolute;left:0;width:100%;top:0;font-family:"Oranienbaum",serif;font-size:40px;color:transparent;-webkit-text-stroke:1px #cfcbcb;letter-spacing:1px}
.section-title .label{position:absolute;left:0;width:100%;top:12px;font-family:"Oranienbaum",serif;font-size:23px;color:var(--ink)}
.on-dark .ghost{-webkit-text-stroke:1px rgba(255,255,255,.2)}
.on-dark .label{color:var(--white)}

/* about */
.about-panel{left:77px;top:485px;width:248px;height:303px;background:var(--gray)}
.about-accent{left:197px;top:485px;width:128px;height:110px;background:var(--terracotta)}
.about-base{left:77px;top:680px;width:123px;height:108px;background:var(--brown)}
.about-strip{left:57px;top:500px;width:14px;height:272px;background:var(--gray)}
.about-strip::after{content:"";position:absolute;left:0;bottom:0;width:14px;height:112px;background:var(--brown)}
.about-side{left:333px;top:497px;width:15px;height:275px;background:var(--gray)}
.about-side::before{content:"";position:absolute;left:0;top:0;width:15px;height:96px;background:var(--terracotta)}
.about-photo{left:98px;top:507px;width:204px;height:258px;border:3px solid var(--white);border-radius:9px;background:linear-gradient(160deg,#d8d6d4,#9fa3a8 45%,#5d7591 75%,#c9c6c2)}
.about-copy{left:362px;top:500px;width:285px;font-size:8px;line-height:16.5px;color:var(--muted)}
.about-copy h2{font-weight:400;font-size:13px;color:var(--terracotta);margin-bottom:6px}
.about-copy p{margin-bottom:16px}
.btn-pill{display:inline-flex;align-items:center;height:28px;border-radius:14px;font-size:8.5px;font-weight:500;padding:0 6px 0 11px;gap:8px}
.btn-pill .arrow{width:10px;height:10px;border-radius:50%;background:var(--white);color:var(--terracotta);font-size:7px;line-height:10px;text-align:center}
.btn-read{background:linear-gradient(90deg,var(--brown) 75%,var(--terracotta) 75%);color:var(--white)}

/* service cards */
.service{top:835px;width:288px;height:246px;border:2px solid var(--terracotta);border-radius:9px}
.service--res{border-color:var(--brown)}
.service-photo{left:10px;top:8px;width:264px;height:225px;border-radius:8px}
.photo-kitchen{background:linear-gradient(180deg,#e9e8e6,#d7d3cf 45%,#b89478 62%,#ecebe9)}
.photo-bath{background:linear-gradient(90deg,#8d9197 0%,#40454c 45%,#b9b8b6 70%,#2a2c2f 100%)}
.service-label{left:-2px;top:213px;width:174px;height:36px;color:var(--white);font-family:"Oranienbaum",serif;font-size:20px;letter-spacing:1px;line-height:36px;text-align:center}
.service--com .service-label{background:var(--terracotta)}
.service--res .service-label{background:var(--brown)}

/* portfolio */
.portfolio{left:0;top:1140px;width:688px;height:435px;background:radial-gradient(circle at 30% 30%,#7a5054,#5d393d 70%)}
.portfolio-frame{left:6px;top:6px;width:676px;height:423px;border:2px solid var(--white)}
.tabs{left:0;top:1209px;width:688px;text-align:center;font-size:8.5px;color:var(--white)}
.tabs span{margin:0 9px}
.tabs .active{color:var(--terracotta)}
.tile{border-radius:6px}
.tile--frame{border:3px solid var(--white)}
.ph-1{background:linear-gradient(160deg,#f1efed,#b6b1ac 55%,#5b5451)}
.ph-2{background:linear-gradient(160deg,#6c6257,#3a3836 45%,#b19a84 70%,#d8d2ca)}
.ph-3{background:linear-gradient(100deg,#b1846a,#d7b79a 45%,#e9e4de 70%,#a59a90)}
.ph-4{background:linear-gradient(150deg,#f2f2f0,#d6dad3 45%,#7b9068 70%,#e6e6e3)}
.tile--brand{background:linear-gradient(180deg,#cf735c,#c0644f);border:2px solid #d88a76;display:flex;align-items:center;justify-content:center;color:var(--white);font-size:15px;letter-spacing:2.5px;font-weight:600}
.btn-view{left:302px;top:1509px;width:84px;background:linear-gradient(90deg,var(--white) 75%,var(--terracotta) 75%);color:var(--brown)}

/* team */
.member{top:1650px;width:137px;height:188px;background:var(--gray);text-align:center}
.member--active{background:var(--brown)}
.avatar{position:absolute;left:22px;top:13px;width:93px;height:93px;border-radius:50%;border:2px solid var(--brown);background:linear-gradient(180deg,#e6e4e2,#c4c0bd)}
.member--active .avatar{border-color:var(--terracotta)}
.member .name{position:absolute;left:0;width:100%;top:116px;font-size:11.5px;font-weight:500;color:var(--ink)}
.member .role{position:absolute;left:0;width:100%;top:134px;font-size:8px;color:var(--terracotta)}
.member--active .name,.member--active .role{color:var(--white)}
.socials{position:absolute;left:0;width:100%;top:155px;display:flex;justify-content:center;gap:6px}
.socials i{width:17px;height:17px;border-radius:50%;border:1.5px solid var(--terracotta)}
.socials i:first-child{background:var(--terracotta)}
.member--active .socials i{border-color:var(--white)}
.member--active .socials i:first-child{background:var(--white)}

/* contact */
.contact{left:0;top:1883px;width:688px;height:312px;background:radial-gradient(circle at 70% 40%,#4a4a4b,#2b2a2b 60%,#1f1e1f)}
.page--b .contact{height:632px}
.contact-title{left:76px;top:1923px;font-family:"Oranienbaum",serif;font-size:22px;color:var(--white)}
.contact-ghost{left:76px;top:1916px;font-family:"Oranienbaum",serif;font-size:38px;color:transparent;-webkit-text-stroke:1px rgba(255,255,255,.12)}
.field{background:var(--white);font-size:8px;color:#555;padding:14px 10px 0}
.btn-send{left:76px;top:2117px;width:132px;height:33px;background:var(--brown);color:#e8dada;font-size:10px;letter-spacing:1px;text-align:center;line-height:33px;font-weight:500}
.diamond{left:385px;top:1905px}

/* footer */
.footer{left:0;top:2195px;width:688px;height:250px;background:var(--black);color:var(--white)}
.page--b .footer{height:320px;background:transparent}
.footer-inner{position:absolute;left:0;top:0;width:688px;height:250px}
.page--b .footer-inner{top:77px}
.foot-brand{left:52px;top:38px;width:120px;text-align:center}
.foot-mark{width:64px;height:64px;border-radius:50%;border:3px solid var(--terracotta);margin:0 auto 10px}
.foot-name{font-size:14px;font-weight:600;color:var(--terracotta);letter-spacing:.5px}
.foot-phone{font-size:11px;color:var(--terracotta);letter-spacing:1px}
.foot-col h3{font-size:11px;font-weight:600;letter-spacing:.3px;margin-bottom:16px}
.foot-links{list-style:none;font-size:8px;line-height:17.6px}
.foot-links li::before{content:"";display:inline-block;width:5px;height:5px;border-radius:50%;background:var(--terracotta);margin-right:8px;vertical-align:1px}
.contact-row{display:flex;align-items:center;gap:9px;font-size:8px;margin-bottom:16px}
.contact-row svg{flex:none}
.news-copy{font-size:8px;line-height:17px;width:158px}
.news-field{font-size:8px;margin-top:4px;padding-bottom:4px;border-bottom:1px solid #bbb;width:156px}
.btn-sub{display:inline-block;margin-top:14px;margin-left:4px;width:82px;height:28px;border-radius:14px;background:var(--terracotta);font-size:9.5px;font-weight:500;text-align:center;line-height:28px}
.foot-rule{left:57px;top:213px;width:574px;border-top:1px solid #4a4647}
.copyright{left:0;top:225px;width:688px;text-align:center;font-size:8px}
</style>
</head>
<body>
<div class="board">

  <section class="page page--a">
    <header class="abs site-header">
      <nav class="abs nav nav--left"><span>HOME</span><span>ABOUT US</span><span>COMMERCIAL</span></nav>
      <div class="abs brand"><span class="brand-mark"></span>MORVELLI TILE</div>
      <nav class="abs nav nav--right"><span>RESIDENTIAL</span><span>PORTFOLIO</span><span>CONTACT</span></nav>
    </header>

    <div class="abs hero" role="img" aria-label="Interior with marble bath, staircase and teal tiled dining wall">
      <svg class="abs" style="left:0;top:0" width="688" height="340" viewBox="0 0 688 340">
        <path d="M270 6 L200 340" stroke="#c96c58" stroke-width="5"/>
        <path d="M470 6 L425 340" stroke="#c96c58" stroke-width="4"/>
      </svg>
      <div class="abs hero-frame"></div>
      <div class="abs hero-box"></div>
      <div class="abs hero-dots"><i></i><i class="on"></i><i class="on"></i><i></i></div>
    </div>
    <div class="abs hero-copy">
      <div class="kicker">WELCOME TO</div>
      <h1>MORVELLI TILE LLC</h1>
      <p>CRAFTED FOR EVERY FLOOR</p>
    </div>

    <div class="abs section-title" style="top:422px"><span class="ghost">ABOUT US</span><span class="label">— ABOUT US —</span></div>
    <div class="abs about-strip"></div>
    <div class="abs about-panel"></div>
    <div class="abs about-accent"></div>
    <div class="abs about-base"></div>
    <div class="abs about-side"></div>
    <div class="abs about-photo" role="img" aria-label="Two tile installers kneeling to check floor tiles in a showroom"></div>
    <div class="abs about-copy">
      <h2>Who we are</h2>
      <p>Sed ut perspiciatis unde omnis iste natus error sit voluptatem accusantium doloremque laudantium, totam rem aperiam.</p>
      <p>eaque ipsa quae ab illo inventore veritatis et quasi architecto beatae vitae dicta sunt explicabo. Nemo enim ipsam voluptatem quia voluptas sit aspernatur aut odit aut fugit, sed quia consequuntur magni dolores eos qui ratione voluptatem sequi nesciunt.</p>
      <p>Neque porro quisquam est, qui dolorem ipsum quia dolor sit amet, consectetur, adipisci velit, sed quia non numquam eius modi tempora incidunt ut labore et dolore magnam aliquam quaerat voluptatem.</p>
      <span class="btn-pill btn-read">Read More <span class="arrow">›</span></span>
    </div>

    <div class="abs service service--com" style="left:44px">
      <div class="abs service-photo photo-kitchen" role="img" aria-label="White kitchen with tiled backsplash and island"></div>
      <div class="abs service-label">COMMERCIAL</div>
    </div>
    <div class="abs service service--res" style="left:348px">
      <div class="abs service-photo photo-bath" role="img" aria-label="Dark bathroom with freestanding tub and herringbone tile wall"></div>
      <div class="abs service-label">RESIDENTIAL</div>
    </div>

    <div class="abs portfolio"><div class="abs portfolio-frame"></div></div>
    <div class="abs section-title on-dark" style="top:1162px"><span class="ghost">PORTFOLIO</span><span class="label">— PORTFOLIO —</span></div>
    <div class="abs tabs"><span class="active">ALL</span><span>RESIDENTIAL</span><span>COMMERCIAL</span></div>
    <div class="abs tile tile--frame ph-1" style="left:57px;top:1241px;width:181px;height:117px" role="img" aria-label="Open living room with staircase"></div>
    <div class="abs tile ph-3" style="left:57px;top:1371px;width:181px;height:119px" role="img" aria-label="Lounge with wood and stone tile walls"></div>
    <div class="abs tile tile--brand" style="left:253px;top:1241px;width:181px;height:249px">MORVELLI TILE</div>
    <div class="abs tile ph-2" style="left:450px;top:1241px;width:181px;height:117px" role="img" aria-label="Dark kitchen with polished tile floor"></div>
    <div class="abs tile ph-4" style="left:450px;top:1371px;width:181px;height:119px" role="img" aria-label="Bright bathroom with plants and white tub"></div>
    <div class="abs btn-pill btn-view">View All <span class="arrow">›</span></div>

    <div class="abs section-title" style="top:1592px"><span class="ghost">OUR TEAM</span><span class="label">— OUR TEAM —</span></div>
    <div class="abs member" style="left:57px"><div class="avatar" role="img" aria-label="Team member portrait"></div><div class="name">Elena</div><div class="role">Director</div><div class="socials"><i></i><i></i><i></i></div></div>
    <div class="abs member member--active" style="left:203px"><div class="avatar" role="img" aria-label="Team member portrait"></div><div class="name">Marcus</div><div class="role">Director</div><div class="socials"><i></i><i></i><i></i></div></div>
    <div class="abs member" style="left:348px"><div class="avatar" role="img" aria-label="Team member portrait"></div><div class="name">Daniel</div><div class="role">Director</div><div class="socials"><i></i><i></i><i></i></div></div>
    <div class="abs member" style="left:494px"><div class="avatar" role="img" aria-label="Team member portrait"></div><div class="name">Sophie Lane</div><div class="role">Director</div><div class="socials"><i></i><i></i><i></i></div></div>

    <div class="abs contact" role="img" aria-label="Dark stacked stone block background"></div>
    <div class="abs contact-ghost">QUICK CONTACT</div>
    <div class="abs contact-title">QUICK CONTACT —</div>
    <div class="abs field" style="left:76px;top:1973px;width:133px;height:32px">First Name</div>
    <div class="abs field" style="left:215px;top:1973px;width:133px;height:32px">Last Name</div>
    <div class="abs field" style="left:76px;top:2012px;width:272px;height:32px">Email Address</div>
    <div class="abs field" style="left:76px;top:2050px;width:272px;height:62px;padding-top:8px">Message</div>
    <div class="abs btn-send">READ MORE</div>
    <svg class="abs diamond" width="250" height="260" viewBox="0 0 250 260" role="img" aria-label="Diamond-cropped bathroom with white tiled frame">
      <defs><linearGradient id="dA" x1="0" y1="0" x2="1" y2="1"><stop offset="0" stop-color="#f1f0ee"/><stop offset=".6" stop-color="#c9c3bd"/><stop offset="1" stop-color="#b48c7c"/></linearGradient></defs>
      <polygon points="122,0 250,128 122,260 0,128" fill="url(#dA)"/>
    </svg>

    <footer class="abs footer">
      <div class="footer-inner">
        <div class="abs foot-brand"><div class="foot-mark"></div><div class="foot-name">MORVELLI TILE</div><div class="foot-phone">(555) 214-0387</div></div>
        <div class="abs foot-col" style="left:202px;top:45px"><h3>QUICK LINKS</h3><ul class="foot-links"><li>Home</li><li>About Us</li><li>Residential</li><li>Commercial</li><li>Contact</li></ul></div>
        <div class="abs foot-col" style="left:307px;top:45px"><h3>CONTACT US</h3>
          <div class="contact-row"><svg width="20" height="20" viewBox="0 0 20 20"><circle cx="10" cy="10" r="10" fill="#c96c58"/><path d="M10 5a3 3 0 0 0-3 3c0 2.3 3 6 3 6s3-3.7 3-6a3 3 0 0 0-3-3z" fill="#fff"/></svg>Ridgeview Utah,84120</div>
          <div class="contact-row"><svg width="20" height="20" viewBox="0 0 20 20"><circle cx="10" cy="10" r="10" fill="#c96c58"/><rect x="5.5" y="7" width="9" height="6.5" fill="#fff"/><path d="M5.5 7l4.5 3.5 4.5-3.5" stroke="#c96c58" fill="none"/></svg>morvelli.tile@mailbox.com</div>
          <div class="contact-row"><svg width="20" height="20" viewBox="0 0 20 20"><circle cx="10" cy="10" r="10" fill="#c96c58"/><path d="M7 5.5l2 2-1 1.5c.6 1.3 1.7 2.4 3 3l1.5-1 2 2-1.3 1.5C9.8 14.3 5.8 10.3 5.5 7z" fill="#fff"/></svg>(555) 214-0387</div>
        </div>
        <div class="abs foot-col" style="left:474px;top:45px"><h3>NEWSLETTER</h3><p class="news-copy">Lorem ipsum dolor sit amet,consectetur adipiscing elit,adipiscing elit.</p><div class="news-field">Email</div><span class="btn-sub">Subscribe</span></div>
        <div class="abs foot-rule"></div>
        <div class="abs copyright">Copyrights@2023.Morvelli Tile.All Rights Reserved</div>
      </div>
    </footer>
  </section>

  <section class="page page--b">
    <header class="abs site-header">
      <nav class="abs nav nav--left"><span>HOME</span><span>ABOUT US</span><span>COMMERCIAL</span></nav>
      <div class="abs brand"><span class="brand-mark"></span>MORVELLI TILE</div>
      <nav class="abs nav nav--right"><span>RESIDENTIAL</span><span>PORTFOLIO</span><span>CONTACT</span></nav>
    </header>

    <div class="abs hero" role="img" aria-label="Interior with marble bath, staircase and teal tiled dining wall">
      <svg class="abs" style="left:0;top:0" width="688" height="340" viewBox="0 0 688 340">
        <path d="M270 6 L200 340" stroke="#c96c58" stroke-width="5"/>
        <path d="M470 6 L425 340" stroke="#c96c58" stroke-width="4"/>
      </svg>
      <div class="abs hero-frame"></div>
      <div class="abs hero-box"></div>
      <div class="abs hero-dots"><i></i><i class="on"></i><i class="on"></i><i></i></div>
    </div>
    <div class="abs hero-copy">
      <div class="kicker">WELCOME TO</div>
      <h1>MORVELLI TILE LLC</h1>
      <p>CRAFTED FOR EVERY FLOOR</p>
    </div>

    <div class="abs section-title" style="top:422px"><span class="ghost">ABOUT US</span><span class="label">— ABOUT US —</span></div>
    <div class="abs about-strip"></div>
    <div class="abs about-panel"></div>
    <div class="abs about-accent"></div>
    <div class="abs about-base"></div>
    <div class="abs about-side"></div>
    <div class="abs about-photo" role="img" aria-label="Two tile installers kneeling to check floor tiles in a showroom"></div>
    <div class="abs about-copy">
      <h2>Who we are</h2>
      <p>Sed ut perspiciatis unde omnis iste natus error sit voluptatem accusantium doloremque laudantium, totam rem aperiam.</p>
      <p>eaque ipsa quae ab illo inventore veritatis et quasi architecto beatae vitae dicta sunt explicabo. Nemo enim ipsam voluptatem quia voluptas sit aspernatur aut odit aut fugit, sed quia consequuntur magni dolores eos qui ratione voluptatem sequi nesciunt.</p>
      <p>Neque porro quisquam est, qui dolorem ipsum quia dolor sit amet, consectetur, adipisci velit, sed quia non numquam eius modi tempora incidunt ut labore et dolore magnam aliquam quaerat voluptatem.</p>
      <span class="btn-pill btn-read">Read More <span class="arrow">›</span></span>
    </div>

    <div class="abs service service--com" style="left:44px">
      <div class="abs service-photo photo-kitchen" role="img" aria-label="White kitchen with tiled backsplash and island"></div>
      <div class="abs service-label">COMMERCIAL</div>
    </div>
    <div class="abs service service--res" style="left:348px">
      <div class="abs service-photo photo-bath" role="img" aria-label="Dark bathroom with freestanding tub and herringbone tile wall"></div>
      <div class="abs service-label">RESIDENTIAL</div>
    </div>

    <div class="abs portfolio"><div class="abs portfolio-frame"></div></div>
    <div class="abs section-title on-dark" style="top:1162px"><span class="ghost">PORTFOLIO</span><span class="label">— PORTFOLIO —</span></div>
    <div class="abs tabs"><span class="active">ALL</span><span>RESIDENTIAL</span><span>COMMERCIAL</span></div>
    <div class="abs tile tile--frame ph-1" style="left:57px;top:1241px;width:181px;height:117px" role="img" aria-label="Open living room with staircase"></div>
    <div class="abs tile ph-3" style="left:57px;top:1371px;width:181px;height:119px" role="img" aria-label="Lounge with wood and stone tile walls"></div>
    <div class="abs tile tile--brand" style="left:253px;top:1241px;width:181px;height:249px">MORVELLI TILE</div>
    <div class="abs tile ph-2" style="left:450px;top:1241px;width:181px;height:117px" role="img" aria-label="Dark kitchen with polished tile floor"></div>
    <div class="abs tile ph-4" style="left:450px;top:1371px;width:181px;height:119px" role="img" aria-label="Bright bathroom with plants and white tub"></div>
    <div class="abs btn-pill btn-view">View All <span class="arrow">›</span></div>

    <div class="abs section-title" style="top:1592px"><span class="ghost">OUR TEAM</span><span class="label">— OUR TEAM —</span></div>
    <div class="abs member" style="left:57px"><div class="avatar" role="img" aria-label="Team member portrait"></div><div class="name">Elena</div><div class="role">Director</div><div class="socials"><i></i><i></i><i></i></div></div>
    <div class="abs member member--active" style="left:203px"><div class="avatar" role="img" aria-label="Team member portrait"></div><div class="name">Marcus</div><div class="role">Director</div><div class="socials"><i></i><i></i><i></i></div></div>
    <div class="abs member" style="left:348px"><div class="avatar" role="img" aria-label="Team member portrait"></div><div class="name">Daniel</div><div class="role">Director</div><div class="socials"><i></i><i></i><i></i></div></div>
    <div class="abs member" style="left:494px"><div class="avatar" role="img" aria-label="Team member portrait"></div><div class="name">Sophie Lane</div><div class="role">Director</div><div class="socials"><i></i><i></i><i></i></div></div>

    <div class="abs contact" role="img" aria-label="Dark stacked stone block background"></div>
    <div class="abs contact-ghost">QUICK CONTACT</div>
    <div class="abs contact-title">QUICK CONTACT —</div>
    <div class="abs field" style="left:76px;top:1973px;width:133px;height:32px">First Name</div>
    <div class="abs field" style="left:215px;top:1973px;width:133px;height:32px">Last Name</div>
    <div class="abs field" style="left:76px;top:2012px;width:272px;height:32px">Email Address</div>
    <div class="abs field" style="left:76px;top:2050px;width:272px;height:62px;padding-top:8px">Message</div>
    <div class="abs btn-send">READ MORE</div>
    <svg class="abs diamond" width="250" height="260" viewBox="0 0 250 260" role="img" aria-label="Diamond-cropped bathroom with white tiled frame">
      <defs><linearGradient id="dB" x1="0" y1="0" x2="1" y2="1"><stop offset="0" stop-color="#f1f0ee"/><stop offset=".6" stop-color="#c9c3bd"/><stop offset="1" stop-color="#b48c7c"/></linearGradient></defs>
      <polygon points="122,0 250,128 122,260 0,128" fill="url(#dB)"/>
    </svg>

    <footer class="abs footer">
      <svg class="abs" style="left:0;top:0" width="688" height="320" viewBox="0 0 688 320">
        <polygon points="0,140 344,12 688,140 688,320 0,320" fill="#c96c58"/>
        <polygon points="0,152 344,26 688,152 688,320 0,320" fill="#161414"/>
      </svg>
      <div class="footer-inner">
        <div class="abs foot-brand"><div class="foot-mark"></div><div class="foot-name">MORVELLI TILE</div><div class="foot-phone">(555) 214-0387</div></div>
        <div class="abs foot-col" style="left:202px;top:45px"><h3>QUICK LINKS</h3><ul class="foot-links"><li>Home</li><li>About Us</li><li>Residential</li><li>Commercial</li><li>Contact</li></ul></div>
        <div class="abs foot-col" style="left:307px;top:45px"><h3>CONTACT US</h3>
          <div class="contact-row"><svg width="20" height="20" viewBox="0 0 20 20"><circle cx="10" cy="10" r="10" fill="#c96c58"/><path d="M10 5a3 3 0 0 0-3 3c0 2.3 3 6 3 6s3-3.7 3-6a3 3 0 0 0-3-3z" fill="#fff"/></svg>Ridgeview Utah,84120</div>
          <div class="contact-row"><svg width="20" height="20" viewBox="0 0 20 20"><circle cx="10" cy="10" r="10" fill="#c96c58"/><rect x="5.5" y="7" width="9" height="6.5" fill="#fff"/><path d="M5.5 7l4.5 3.5 4.5-3.5" stroke="#c96c58" fill="none"/></svg>morvelli.tile@mailbox.com</div>
          <div class="contact-row"><svg width="20" height="20" viewBox="0 0 20 20"><circle cx="10" cy="10" r="10" fill="#c96c58"/><path d="M7 5.5l2 2-1 1.5c.6 1.3 1.7 2.4 3 3l1.5-1 2 2-1.3 1.5C9.8 14.3 5.8 10.3 5.5 7z" fill="#fff"/></svg>(555) 214-0387</div>
        </div>
        <div class="abs foot-col" style="left:474px;top:45px"><h3>NEWSLETTER</h3><p class="news-copy">Lorem ipsum dolor sit amet,consectetur adipiscing elit,adipiscing elit.</p><div class="news-field">Email</div><span class="btn-sub">Subscribe</span></div>
        <div class="abs foot-rule"></div>
        <div class="abs copyright">Copyrights@2023.Morvelli Tile.All Rights Reserved</div>
      </div>
    </footer>
  </section>

</div>
</body>
</html>
```